New Business Card for Casual Beachfront Cafe

Quirky Beachfront Cafe at Moana, South Australia needs a DOUBLE SIDED business card to print on PrintHarbor.

Target Market(s)

Business Cards sit on the counter for Guests to take with them. Please view our website www.saltreefcafe.com.au to get a feel for the Cafe. You may also view our Instagram at @saltreefcafe

Industry/Entity Type

Cafe / Restaurant

Contact Information for Business Card

Information equivalent to: Breakfast, Lunch, Dinner, Coffee, Takeaway / 117 Parade Moana SA 5169 / Menu & Opening Hours: www.saltreefcafe.com.au / ph (08) 8461 9273

Requirements
Must have
• Information equivalent to: Breakfast, Lunch, Dinner, Coffee, Takeaway / 117 Parade Moana SA 5169 / Menu & Opening Hours: www.saltreefcafe.com.au / ph (08) 8461 9273
Nice to have
• Potentially some of our trademark colours (Cafe can be searched via Seekly)
Should not have
• Must NOT have image of the building. May have the logo provided on one side but not necessarily, depending on how you wish to design the card

```html
<!DOCTYPE html>
<html lang="en">
<head>
<meta charset="utf-8">
<title>Salt Reef Cafe – Business Card</title>
<link rel="stylesheet" href="https://fonts.googleapis.com/css2?family=Montserrat:wght@500;700;800&display=swap">
<style>
  :root {
    --navy: #1b4683;
    --navy-dark: #163a6e;
    --sun: #f7e600;
    --rust: #c0541c;
    --ink: #555a63;
    --paper: #ffffff;
    --backdrop: #e9e7e3;
  }
  * { box-sizing: border-box; margin: 0; padding: 0; }
  html, body { width: 1200px; height: 913px; overflow: hidden; }
  body {
    background: var(--backdrop);
    font-family: "Montserrat", Arial, sans-serif;
    display: flex; flex-direction: column; align-items: center; justify-content: center;
    gap: 36px;
  }
  .card {
    width: 640px; height: 390px; border-radius: 22px;
    position: relative; overflow: hidden;
    box-shadow: 0 6px 18px rgba(0,0,0,.18);
  }
  .card-front { background: var(--navy); display: flex; align-items: center; justify-content: center; }
  .brand-name {
    font-weight: 800; text-transform: uppercase; letter-spacing: 1px; line-height: 1;
    text-align: center;
  }
  .card-front .brand-name { color: var(--sun); font-size: 64px; }
  .card-back { background: var(--paper); }
  .card-back .brand-name {
    color: var(--navy); font-size: 50px;
    position: absolute; top: 58px; left: 0; right: 0;
  }
  .details {
    position: absolute; top: 170px; left: 0; right: 0;
    display: flex; justify-content: center; align-items: center; gap: 22px;
  }
  .hours { text-align: right; }
  .hours-label { color: var(--navy); font-weight: 700; font-size: 16px; letter-spacing: .5px; }
  .website { color: var(--ink); font-weight: 500; font-size: 16px; margin-top: 8px; letter-spacing: .3px; }
  .divider { width: 1.5px; height: 52px; background: var(--navy); }
  .contact { list-style: none; }
  .contact li {
    display: flex; align-items: center; gap: 7px;
    color: var(--ink); font-weight: 500; font-size: 16px; letter-spacing: .3px;
  }
  .contact li + li { margin-top: 8px; }
  .contact svg { width: 15px; height: 15px; fill: var(--navy); flex: none; }
  .service-band {
    position: absolute; left: 0; right: 0; bottom: 34px; height: 46px;
    background: var(--sun);
    border-top: 2px solid var(--rust); border-bottom: 2px solid var(--rust);
    display: flex; align-items: center; justify-content: center; gap: 14px;
    color: var(--navy); font-weight: 700; font-size: 18px; letter-spacing: 1px;
    text-transform: uppercase;
  }
  .service-band .sep { color: var(--rust); font-size: 16px; }
  .band-tail { position: absolute; left: 0; right: 0; bottom: 0; height: 34px; background: var(--sun); }
</style>
</head>
<body>
  <section class="card card-front" aria-label="Card front">
    <h1 class="brand-name">Salt Reef<br>Cafe</h1>
  </section>

  <section class="card card-back" aria-label="Card back">
    <h2 class="brand-name">Salt Reef Cafe</h2>

    <div class="details">
      <div class="hours">
        <p class="hours-label">Opening Hours:</p>
        <p class="website">www.saltreefcafe.com.au</p>
      </div>
      <span class="divider"></span>
      <ul class="contact">
        <li>
          <svg viewBox="0 0 24 24" aria-hidden="true"><path d="M6.6 10.8a15.1 15.1 0 0 0 6.6 6.6l2.2-2.2a1 1 0 0 1 1-.25 11.4 11.4 0 0 0 3.6.57 1 1 0 0 1 1 1V20a1 1 0 0 1-1 1A17 17 0 0 1 3 4a1 1 0 0 1 1-1h3.5a1 1 0 0 1 1 1c0 1.25.2 2.45.57 3.57a1 1 0 0 1-.25 1z"/></svg>
          (08) 8461 9273
        </li>
        <li>
          <svg viewBox="0 0 24 24" aria-hidden="true"><path d="M12 2a7 7 0 0 0-7 7c0 5.25 7 13 7 13s7-7.75 7-13a7 7 0 0 0-7-7zm0 9.5A2.5 2.5 0 1 1 12 6.5a2.5 2.5 0 0 1 0 5z"/></svg>
          117 Parade Moana SA 5169
        </li>
      </ul>
    </div>

    <div class="service-band">
      <span>Breakfast</span><span class="sep">›</span>
      <span>Lunch</span><span class="sep">›</span>
      <span>Dinner</span><span class="sep">›</span>
      <span>Coffee</span><span class="sep">›</span>
      <span>Takeaway</span>
    </div>
    <div class="band-tail"></div>
  </section>
</body>
</html>
```